Lantern Ridge Tile Inc. Business Card

Looking for business card with embossed raised logo print. Logo provided and want it to be most prominent image on card. Color pallet of black, red, white or charcoal gray preferred for brand recognition. Simple contact information on front and list description of services provided on back. Services included....Custom Showers, Tub Surrounds, Backsplashes, Fireplaces, Floors and more. Dustless Demolition, Lifetime Warranty, Proud member of the Federated Stoneworks Trade Guild

Target Market(s)

High end residential remodel work and new home builders

Contact Information for Business Card

Phone # (402) 555-0193 email address, Lanternridgets@mailvane.net Colby Hanswirth Owner

Requirements
Must have
• Business logo as most prominent image on the front of business card. Along with contact information and name Colby Hanswirth. Would like to see services provided on the back of the card.

```html
<!DOCTYPE html>
<html lang="en">
<head>
<meta charset="utf-8">
<title>Lantern Ridge Tile Inc. Business Card</title>
<link href="https://fonts.googleapis.com/css2?family=Roboto:wght@400;500;700&display=swap" rel="stylesheet">
<style>
  :root {
    --stage: #2b2b2d;
    --card: #1a1a1b;
    --card-edge: #232325;
    --emboss: #262628;
    --emboss-line: #303033;
    --red: #c8202a;
    --white: #f2f2f2;
    --grey: #a9a9ab;
  }
  * { margin: 0; padding: 0; box-sizing: border-box; }
  html, body { width: 1200px; height: 889px; overflow: hidden; }
  body {
    background: var(--stage);
    font-family: "Roboto", Arial, sans-serif;
    position: relative;
  }
  .card {
    position: absolute;
    width: 520px;
    height: 297px;
    background: var(--card);
    border: 1px solid var(--card-edge);
    border-radius: 3px;
    box-shadow: 0 18px 40px rgba(0,0,0,0.45);
    overflow: hidden;
  }
  .card-front { left: 90px; top: 140px; }
  .card-back { left: 590px; top: 452px; }

  .emboss-mark {
    position: absolute;
    width: 150px;
    height: 150px;
    background: var(--emboss);
    border: 1px solid var(--emboss-line);
  }
  .card-front .emboss-mark { right: 40px; top: 30px; }
  .card-back .emboss-mark { left: 40px; bottom: 40px; }

  .brand {
    position: absolute;
    left: 40px;
    bottom: 58px;
    display: flex;
    align-items: center;
    gap: 10px;
  }
  .brand-square {
    width: 30px;
    height: 30px;
    background: var(--red);
  }
  .brand-name {
    color: var(--red);
    font-weight: 500;
    font-size: 24px;
    letter-spacing: 1px;
    text-transform: uppercase;
  }

  .contact {
    position: absolute;
    right: 30px;
    top: 26px;
    text-align: right;
  }
  .person-name {
    color: var(--red);
    font-weight: 700;
    font-size: 17px;
    letter-spacing: 0.5px;
    text-transform: uppercase;
  }
  .person-title {
    color: var(--white);
    font-weight: 700;
    font-size: 11px;
    margin-top: 2px;
  }
  .contact-list {
    list-style: none;
    margin-top: 14px;
  }
  .contact-list li {
    color: var(--grey);
    font-size: 11px;
    line-height: 15px;
    display: flex;
    justify-content: flex-end;
    align-items: center;
    gap: 6px;
  }
  .contact-list svg { width: 9px; height: 9px; fill: var(--red); }

  .services {
    position: absolute;
    right: 30px;
    top: 150px;
    text-align: right;
    color: var(--grey);
    font-size: 11.5px;
    line-height: 17px;
  }
  .services .dot { color: var(--red); padding: 0 3px; }
</style>
</head>
<body>

<section class="card card-front">
  <div class="emboss-mark" role="img" aria-label="Blind-embossed brand mark"></div>
  <div class="brand">
    <span class="brand-square"></span>
    <span class="brand-name">Lantern Ridge Tile Inc</span>
  </div>
</section>

<section class="card card-back">
  <div class="emboss-mark" role="img" aria-label="Blind-embossed brand mark"></div>
  <div class="contact">
    <p class="person-name">Colby Hanswirth</p>
    <p class="person-title">President</p>
    <ul class="contact-list">
      <li>(402) 555-0193
        <svg viewBox="0 0 10 10"><path d="M2 0.5 L4 2.5 L3 4 Q4.5 6 6 7 L7.5 6 L9.5 8 L8 9.5 Q3.5 9 0.5 2 Z"/></svg>
      </li>
      <li>Lanternridgets@mailvane.net
        <svg viewBox="0 0 10 10"><rect x="0.5" y="2" width="9" height="6" rx="1"/></svg>
      </li>
      <li>www.Lanternridgets.net
        <svg viewBox="0 0 10 10"><circle cx="5" cy="5" r="4.5"/></svg>
      </li>
    </ul>
  </div>
  <div class="services">
    <p>Custom Showers<span class="dot">•</span>Tub Surrounds<span class="dot">•</span>Backsplashes</p>
    <p>Fireplaces<span class="dot">•</span>Floors &amp; more<span class="dot">•</span>Dustless Demolition<span class="dot">•</span>Lifetime Warranty</p>
    <p>Proud member of the Federated Stoneworks Trade Guild</p>
  </div>
</section>

</body>
</html>
```